Bright Oak Fitness Facility Business Cards

Business Card Design that incorporates the logo and tagline

Target Market(s)

Fitness, People Who Exercise

Contact Information for Business Card

2817 Mossgrove Bend Road
Tavares, Florida 32190
Phone: 352-555-Jump (5867)
www.brightoakfitness.example
info@brightoakfitness.example

Requirements
Must have
• Logo, Address, Website, email and tagline "More Than A Gym". Colors should be red/black/grey/white

```html
<!DOCTYPE html>
<html lang="en">
<head>
<meta charset="utf-8">
<title>Bright Oak Fitness – Business Card</title>
<link rel="stylesheet" href="https://fonts.googleapis.com/css2?family=Tinos&family=Poiret+One&display=swap">
<style>
  :root {
    --page: #ffffff;
    --card: #231f20;
    --red: #ed1c24;
    --white: #ffffff;
  }
  html, body {
    margin: 0;
    padding: 0;
    width: 1200px;
    height: 1200px;
    overflow: hidden;
    background: var(--page);
  }
  .canvas {
    position: relative;
    width: 1200px;
    height: 1200px;
  }
  .business-card {
    position: absolute;
    left: 214px;
    top: 379px;
    width: 772px;
    height: 442px;
    background: var(--card);
    overflow: hidden;
  }
  .brand-name {
    position: absolute;
    left: 52px;
    top: 116px;
    margin: 0;
    font-family: "Tinos", "Times New Roman", serif;
    font-weight: 400;
    font-size: 30px;
    line-height: 1;
    color: var(--white);
  }
  .emblem-area {
    position: absolute;
    left: 520px;
    top: 40px;
    width: 200px;
    height: 200px;
    background: var(--red);
  }
  .contact {
    position: absolute;
    left: 52px;
    top: 236px;
    margin: 0;
    font-family: "Tinos", "Times New Roman", serif;
    font-size: 21px;
    line-height: 25.6px;
    color: var(--white);
    font-style: normal;
  }
  .contact p { margin: 0; }
  .contact .address { margin-bottom: 26px; }
  .tagline {
    position: absolute;
    left: 439px;
    top: 310px;
    margin: 0;
    font-family: "Poiret One", "Futura", sans-serif;
    font-size: 32px;
    line-height: 1;
    letter-spacing: 1px;
    word-spacing: 10px;
    color: var(--red);
    white-space: nowrap;
  }
</style>
</head>
<body>
<div class="canvas">
  <section class="business-card">
    <h1 class="brand-name">Bright Oak Fitness</h1>
    <div class="emblem-area" role="img" aria-label="Brand emblem area"></div>
    <address class="contact">
      <div class="address">
        <p>2817 Mossgrove Bend Road</p>
        <p>Tavares, Florida 32190</p>
      </div>
      <p>Phone : 352-555-Jump (5867)</p>
      <p>Email : info@brightoakfitness.example</p>
      <p>Website : www.brightoakfitness.example</p>
    </address>
    <p class="tagline">More Than A Gym</p>
  </section>
</div>
</body>
</html>
```